Professional Engineering Web Design

Project Brief: Website Redesign for Mechanical Design Consultancy
Project Overview
I want to update and improve my current website to create a more professional, modern, and high-credibility online presence for my mechanical design consultancy.

Current site: https://valtrobuild.design/

The new website must communicate expertise, precision, and trust—matching the standard of top engineering and product design agencies.

Reference Websites (Style + Structure Inspiration)
These represent the quality, cleanliness, and professionalism I want to achieve:

https://plinthformworks.com/
https://www.zorvanta.com/
https://quellory-uk.com/
Brand Look
Professional, modern, engineering-focused aesthetic
Clean layouts and strong typography
High-quality imagery conveying precision, innovation, and mechanical expertise
Colour scheme and styling must follow my existing logo (attached in project)
Platform Requirements
The website must be built on WordPress
Should use a clean, flexible theme or modern page builder (Elementor, Gutenberg, Bricks, or similar)
Avoid overly complex custom coding so I can easily edit content later
Final deliverable must allow me to manage and update content without developer assistance
Functionality
Fast-loading, lightweight, and smooth user experience
Clean animations and transitions similar to the reference sites
Fully mobile responsive
Clear navigation and strong visual hierarchy
Contact forms optimised for lead generation
Optional: subtle scroll effects, case study sliders, icon animations, etc.
SEO Aspirations
Developer should recommend and implement a modern SEO strategy
Proper on-page SEO setup (titles, meta, schema, alt tags, heading structure)
Optimised site architecture for ranking and crawling
Aim: Generate leads through improved visibility and keyword targeting
Optional but useful: Google Analytics, Google Search Console setup
User Journeys
(Recommended structure)

The site should be crafted around clear, intuitive journeys for each type of visitor:

Potential new clients
Quickly understand what services I offer
View examples of past work / case studies
See credibility indicators (process, expertise, industries served)
Easily contact me or request a project discussion
Returning clients
Access updated portfolio items
Find contact details or book follow-up work easily
General visitors discovering through SEO
Be guided to core service areas
Understand my value proposition quickly
Be invited to learn more or make contact
The developer should design the structure to support these journeys smoothly.

Maintenance Expectations
Website will be maintained by me, so it should be easy to update using relatively basic WordPress skills
Use modular templates and simple backend structure
Avoid unnecessary plugins
Provide brief handover documentation if required
Hosting Preferences
Site is currently hosted via a family member
Open to discussing moving to a paid, reliable hosting provider if preferable for performance and maintainability
Developer may advise on the best hosting setup for WordPress
Content
Most content can be taken from the existing website
Developer is welcome to suggest improvements to structure, layout, and imagery
Must remain easy for me to edit or add new content later (e.g., new projects)
Deliverables
Fully built WordPress website
Clean, professional, modern design inspired by the reference sites
Mobile-responsive across all devices
SEO-ready structure and optimisations
Transfer of website and admin rights
Any design assets, templates, or documentation used

```html
<!DOCTYPE html>
<html lang="en">
<head>
<meta charset="utf-8">
<title>Valtro Build – Mechanical CAD Design</title>
<link href="https://fonts.googleapis.com/css2?family=Inter:ital,wght@0,400;0,500;0,600;0,700;0,800;1,400&display=swap" rel="stylesheet">
<style>
:root{
  --blue:#2f55f0;
  --blue-dark:#1d3fd6;
  --navy:#0a1240;
  --ink:#141414;
  --text:#333;
  --muted:#666;
  --line:#c9c9c9;
  --tint:#e8ecf8;
  --white:#fff;
}
*{box-sizing:border-box;margin:0;padding:0}
html,body{width:1200px;height:4979px;overflow:hidden}
body{position:relative;background:var(--white);font-family:"Inter",sans-serif;color:var(--text)}
.abs{position:absolute}
.btn{position:absolute;display:flex;align-items:center;justify-content:center;gap:10px;border-radius:24px;font-size:14px;font-weight:600;color:var(--white);background:var(--blue);text-decoration:none}
.btn-ghost{background:transparent;border:1.5px solid rgba(255,255,255,.85)}
.hl{background:var(--tint);padding:0 8px}
.section-title{position:absolute;left:0;width:1200px;text-align:center;font-weight:800;color:var(--ink);letter-spacing:-.5px}
.section-sub{position:absolute;left:300px;width:600px;text-align:center;font-size:14px;line-height:21px;color:var(--ink)}

/* top bar */
.topbar{left:464px;top:0;width:736px;height:28px;background:var(--blue);border-bottom-left-radius:6px;display:flex;align-items:center;gap:48px;padding-left:28px;font-size:11px;color:var(--white);z-index:3}
.topbar span{display:flex;align-items:center;gap:7px}

/* header */
.site-header{left:0;top:0;width:1200px;height:98px;background:var(--white);z-index:2}
.brand{left:139px;top:50px;display:flex;align-items:center;gap:10px;z-index:4}
.brand-mark{width:20px;height:20px;background:var(--blue)}
.brand-name{font-size:24px;font-weight:700;color:var(--ink);line-height:28px}
.main-nav{left:384px;top:57px;display:flex;gap:38px;font-size:14.5px;color:#222;z-index:3}
.search{left:792px;top:46px;width:257px;height:42px;border:1px solid var(--line);border-radius:22px;display:flex;align-items:center;justify-content:space-between;padding:0 14px 0 26px;font-size:13px;color:#aaa;z-index:3}

/* hero */
.hero{left:0;top:98px;width:1200px;height:632px;background:radial-gradient(ellipse at 78% 85%,#b87a2a 0,#5a4a3a 18%,transparent 40%),linear-gradient(160deg,#16254f 0%,#1f3f7a 40%,#142a5a 70%,#0c1a3a 100%);overflow:hidden}
.hero-title{top:128px;left:0;width:1200px;text-align:center}
.hero-title h1{display:inline-block;font-size:66px;font-weight:800;color:var(--white);background:rgba(12,24,60,.55);padding:0 8px;line-height:74px;letter-spacing:-.5px}
.hero-sub{top:214px;left:205px;width:790px;text-align:center;font-size:14.5px;line-height:22px;color:var(--white)}
.hero-curve{left:0;bottom:0;width:1200px;height:120px}

/* intro */
.about-visual{left:150px;top:902px;width:400px;height:425px}
.about-ring{left:0;top:40px;width:380px;height:380px;border-radius:50%;border:58px solid var(--blue)}
.about-photo{left:28px;top:0;width:340px;height:425px;border-radius:0 0 40px 40px;background:linear-gradient(180deg,#c9a27a 0%,#e07a22 45%,#3f4552 80%,#2b2f38 100%)}
.about-copy{left:653px;top:928px;width:400px}
.about-copy h2{display:flex;align-items:center;gap:12px;font-size:34px;font-weight:800;color:var(--ink);margin-bottom:22px}
.about-copy h2 i{width:38px;height:38px;border-radius:50%;background:var(--blue);display:block}
.about-copy p{font-size:13px;line-height:22px;color:var(--text);margin-bottom:23px}

/* stats */
.stats-band{left:0;top:1327px;width:1200px;height:390px;background:linear-gradient(180deg,#fff 0%,#d9dbe0 18%,#8b909a 45%,#5e6470 75%,#3d424c 100%)}
.stat{top:1395px;height:98px;background:rgba(255,255,255,.92);border-radius:4px;padding:14px 0 0 30px}
.stat::before{content:"";position:absolute;left:16px;top:14px;width:3px;height:70px;background:var(--blue)}
.stat b{display:block;font-size:50px;font-weight:600;color:var(--ink);line-height:52px}
.stat span{font-size:14px;color:#444}

/* work */
.work-card{top:1945px;width:284px;height:435px;background:var(--blue);border-radius:2px;overflow:hidden;color:var(--white);text-align:center}
.work-img{width:100%;height:219px}
.icon-disc{position:absolute;left:94px;top:171px;width:96px;height:96px;border-radius:50%;background:var(--white);display:flex;align-items:center;justify-content:center}
.work-card h3{margin-top:74px;font-size:19px;font-weight:700}
.work-card p{margin:8px auto 0;width:230px;font-size:13px;line-height:21px}
.arrow{width:56px;height:56px;border-radius:50%;border:1.5px solid #666;background:var(--white);display:flex;align-items:center;justify-content:center}

/* expertise */
.expertise-bg{left:0;top:2517px;width:1200px;height:661px;background:radial-gradient(ellipse at 88% 30%,#4a6db8 0,transparent 35%),linear-gradient(120deg,#1b3f9c 0%,#14307a 45%,#0e1f52 100%)}
.exp-card{top:2736px;width:294px;height:253px;background:var(--white);border-radius:14px;text-align:center;padding-top:34px}
.exp-icon{width:98px;height:98px;border-radius:50%;background:var(--blue);margin:0 auto;display:flex;align-items:center;justify-content:center}
.exp-card h3{margin-top:26px;font-size:19px;font-weight:600;color:var(--ink)}
.exp-card p{margin:10px auto 0;width:260px;font-size:13px;line-height:21px;color:#333}

/* reviews */
.review{top:3526px;width:284px;height:355px;border:1.5px solid #bdbdbd;text-align:center}
.review-mark{position:absolute;left:126px;top:-17px;width:32px;height:32px;border-radius:50%;background:var(--white);border:3px solid #9aa0a6}
.stars{margin-top:38px;display:flex;justify-content:center;gap:3px}
.review p{margin:12px auto 0;width:220px;font-size:10.5px;line-height:19.5px;font-style:italic;color:#555}
.avatar{position:absolute;left:118px;top:270px;width:48px;height:48px;border-radius:50%;background:linear-gradient(180deg,#6b5a4e,#d9c2ae)}
.review h4{position:absolute;left:0;width:100%;top:324px;font-size:13px;font-weight:500;color:#222;line-height:20px}

/* trust */
.trust{left:145px;top:3941px;width:904px;height:474px;background:var(--blue);border-radius:18px}
.trust h2{position:absolute;left:42px;top:66px;font-size:33px;font-weight:600;color:var(--white);line-height:40px}
.trust .lead{position:absolute;left:42px;top:152px;width:390px;font-size:13.5px;line-height:21px;color:var(--white)}
.feature{position:absolute;display:flex;gap:14px;color:var(--white);width:200px}
.feature i{flex:none;width:40px;height:40px;border-radius:8px;background:var(--white);display:flex;align-items:center;justify-content:center}
.feature b{display:block;font-size:12px;font-weight:700;margin-bottom:3px}
.feature span{font-size:11px;line-height:14px;display:block;opacity:.9}
.chart-card{position:absolute;left:477px;top:31px;width:404px;height:414px;background:var(--white);border-radius:16px;text-align:center}
.chart-card h3{margin-top:44px;font-size:19px;font-weight:600;color:var(--ink)}
.chart-card p{position:absolute;left:0;width:100%;top:366px;font-size:12.5px;line-height:17px;font-weight:600;color:#222}

/* footer */
.footer{left:0;top:4520px;width:1200px;height:459px;background:var(--navy)}
.footer-curve{left:0;top:4460px;width:1200px;height:130px}
.footer-brand{left:145px;top:4640px;display:flex;align-items:center;gap:10px}
.footer-brand i{width:20px;height:20px;background:var(--blue)}
.footer-brand span{font-size:24px;font-weight:700;color:var(--white);line-height:28px}
.footer-about{left:145px;top:4710px;width:320px;font-size:13px;line-height:21px;color:var(--white)}
.socials{left:145px;top:4800px;display:flex;gap:26px;padding-bottom:10px;border-bottom:1px solid rgba(255,255,255,.5);width:170px}
.socials i{width:16px;height:16px;border-radius:50%;background:var(--white)}
.footer-col{top:4668px;font-size:13px;color:var(--white)}
.footer-col h5{font-size:13px;font-weight:600;text-decoration:underline;margin-bottom:25px}
.footer-col li{list-style:none;line-height:21px}
.legal-line{top:4930px;font-size:11px;color:var(--white)}
</style>
</head>
<body>

<div class="abs topbar">
  <span><svg width="10" height="12" viewBox="0 0 10 12"><path d="M5 0a4 4 0 0 0-4 4c0 3 4 8 4 8s4-5 4-8a4 4 0 0 0-4-4zm0 5.5A1.5 1.5 0 1 1 5 2.5a1.5 1.5 0 0 1 0 3z" fill="#fff"/></svg>We're based in South Wales, UK.</span>
  <span><svg width="11" height="11" viewBox="0 0 12 12"><path d="M2.5 1l2 2.5-1.2 1.3a7 7 0 0 0 3.9 3.9L8.5 7.5 11 9.5 9.8 11C5 11 1 7 1 2.2z" fill="#fff"/></svg>+44 (0) 7700 900123</span>
  <span><svg width="12" height="11" viewBox="0 0 12 11"><path d="M0 5L12 0 9 11 6 7z" fill="#fff"/></svg>info@valtrobuild.design</span>
</div>

<header class="abs site-header"></header>
<div class="abs brand"><span class="brand-mark"></span><span class="brand-name">Valtro Build</span></div>
<nav class="abs main-nav"><span>Services</span><span>Portfolio</span><span>Process</span><span>About</span></nav>
<div class="abs search">Search<svg width="22" height="22" viewBox="0 0 22 22"><circle cx="9" cy="9" r="7" fill="none" stroke="#333" stroke-width="1.8"/><path d="M14 14l6 6" stroke="#333" stroke-width="1.8"/></svg></div>

<section class="abs hero" role="img" aria-label="Glowing blue circuit board with golden mechanical gears">
  <div class="abs hero-title"><h1>MECHANICAL CAD DESIGN</h1></div>
  <p class="abs hero-sub">From concept to fully manufacturable product I provide expert mechanical design that solves complex engineering challenges with accuracyand efficiency.</p>
  <a class="btn" style="left:361px;top:277px;width:228px;height:46px"><svg width="18" height="18"><circle cx="9" cy="9" r="8" fill="#fff"/></svg>Start Your Project</a>
  <a class="btn btn-ghost" style="left:605px;top:277px;width:230px;height:48px">View Case Studies</a>
  <svg class="abs hero-curve" viewBox="0 0 1200 120" preserveAspectRatio="none"><path d="M0 55C400 48 820 30 1200 0V40C820 62 400 85 0 100Z" fill="#2f55f0"/><path d="M0 100C400 85 820 62 1200 40V120H0Z" fill="#fff"/></svg>
</section>

<h2 class="section-title" style="top:786px;font-size:42px;line-height:50px">PRECISION RELIABILITY PRACTICAL<br><span class="hl">ENGINEERING.</span></h2>

<div class="abs about-visual" role="img" aria-label="Two engineers in hi-vis vests reviewing a laptop on site">
  <div class="abs about-ring"></div>
  <div class="abs about-photo"></div>
</div>
<div class="abs about-copy">
  <h2><i></i>ABOUT US</h2>
  <p>Daniel Marsh is the Chief Engineer at Valtro Build Mechanical Design. He has 11 years experience working as a mechanical design engineer in multiple industries icluing high performance automotive,</p>
  <p>consumer products, medical, industrial plus many more. He has worked in multiple roles across a wide range of products.</p>
  <p>Valtro Build Design provides professional mechanical engineering &amp; product development support for companies that require accurate, productionready design. With experience across multiple industries</p>
</div>
<a class="btn" style="left:653px;top:1285px;width:228px;height:48px">Tell us about your ideas</a>

<div class="abs stats-band" role="img" aria-label="Close-up of a precision gearbox assembly"></div>
<div class="abs stat" style="left:145px;width:193px"><b>15+</b><span>Years Experience</span></div>
<div class="abs stat" style="left:384px;width:192px"><b>200+</b><span>Projects Delivered</span></div>
<div class="abs stat" style="left:624px;width:187px"><b>100%</b><span>Client Satisfaction</span></div>
<div class="abs stat" style="left:858px;width:191px"><b>50+</b><span>Industries Served</span></div>

<h2 class="section-title" style="top:1786px;font-size:50px;line-height:60px"><span class="hl">OUR WORK</span></h2>
<p class="section-sub" style="top:1868px;left:280px;width:640px">Explore a range of projects demonstrating our expertise in CAD modeling, mechanical design, and engineering for manufacture.</p>

<div class="abs arrow" style="left:63px;top:2134px"><svg width="14" height="14"><path d="M9 2L4 7l5 5" fill="none" stroke="#222" stroke-width="2.2"/></svg></div>
<div class="abs arrow" style="left:1069px;top:2134px"><svg width="14" height="14"><path d="M5 2l5 5-5 5" fill="none" stroke="#222" stroke-width="2.2"/></svg></div>

<article class="abs work-card" style="left:145px">
  <div class="work-img" role="img" aria-label="White sports car with custom alloy wheels" style="background:linear-gradient(180deg,#e9ecef,#9aa1aa 60%,#5d636c)"></div>
  <div class="icon-disc"><svg width="50" height="50" viewBox="0 0 50 50"><circle cx="25" cy="25" r="20" fill="none" stroke="#333" stroke-width="3"/><circle cx="25" cy="25" r="6" fill="#333"/><path d="M25 7v12M25 31v12M7 25h12M31 25h12" stroke="#333" stroke-width="3"/></svg></div>
  <h3>3-Piece Alloy Wheels</h3>
  <p>We have been working on a long term project to bring custom 3-piece Japanese style wheels to market since 2020.</p>
</article>
<article class="abs work-card" style="left:456px">
  <div class="work-img" role="img" aria-label="Go-kart racing on a circuit" style="background:linear-gradient(180deg,#c8d0d8,#8a9a84 55%,#59604f)"></div>
  <div class="icon-disc"><svg width="50" height="50" viewBox="0 0 50 50"><path d="M8 34h34l-4-10H20l-4-8" fill="none" stroke="#333" stroke-width="3"/><circle cx="14" cy="36" r="5" fill="#333"/><circle cx="38" cy="36" r="5" fill="#333"/></svg></div>
  <h3>Go-Kart Simulator Design</h3>
  <p>Our client already had an existing product, but wanted it updating and refreshing to offer their customers a better product.</p>
</article>
<article class="abs work-card" style="left:765px">
  <div class="work-img" role="img" aria-label="Engineer in hard hat inspecting electrical switchgear" style="background:linear-gradient(180deg,#8d949c,#b4c04a 55%,#4e5560)"></div>
  <div class="icon-disc"><svg width="50" height="50" viewBox="0 0 50 50"><rect x="8" y="13" width="28" height="24" rx="3" fill="none" stroke="#333" stroke-width="3"/><rect x="14" y="19" width="8" height="12" fill="#333"/><circle cx="38" cy="34" r="6" fill="none" stroke="#333" stroke-width="3"/></svg></div>
  <h3>Electrical Switchgear</h3>
  <p>In the UK a lot of electrical switchgear in grid sub-stations are very old, many of them originating in the 60s. In this time maintenance was all manual</p>
</article>
<a class="btn" style="left:483px;top:2421px;width:228px;height:46px">See All Project</a>

<section class="abs expertise-bg" role="img" aria-label="Engineer working at a computer in a dimly lit studio"></section>
<svg class="abs" style="left:0;top:3088px" width="1200" height="92" viewBox="0 0 1200 92" preserveAspectRatio="none"><path d="M0 0C300 40 700 50 1200 30V60C700 80 300 70 0 40Z" fill="#2f55f0"/><path d="M0 40C300 70 700 80 1200 60V92H0Z" fill="#fff"/></svg>
<h2 class="section-title" style="top:2570px;font-size:50px;line-height:60px;color:#fff"><span class="hl" style="background:#1a3aa8">OUR EXPERTISE</span></h2>
<p class="section-sub" style="top:2650px;color:#fff">We provide expert mechanical design, CAD engineering, and manufacturing ready solutions for products of all complexities.</p>

<div class="abs exp-card" style="left:147px">
  <div class="exp-icon"><svg width="48" height="48" viewBox="0 0 48 48"><rect x="10" y="8" width="28" height="8" rx="2" fill="#fff"/><rect x="12" y="18" width="24" height="18" rx="2" fill="none" stroke="#fff" stroke-width="3"/><path d="M18 27l6-4 6 4-6 4z" fill="#fff"/><rect x="8" y="38" width="32" height="4" fill="#fff"/></svg></div>
  <h3>Bespoke Product Design</h3>
  <p>Innovative design from concept through the full development life cycle</p>
</div>
<div class="abs exp-card" style="left:450px">
  <div class="exp-icon"><svg width="48" height="48" viewBox="0 0 48 48"><rect x="6" y="8" width="36" height="26" rx="3" fill="none" stroke="#fff" stroke-width="3"/><circle cx="17" cy="21" r="5" fill="#fff"/><path d="M27 16h10M27 22h10M27 28h6M16 40h16" stroke="#fff" stroke-width="3"/></svg></div>
  <h3>3D Modelling and Drawings</h3>
  <p>We create 3D CAD, 2D engineering drawings and photorealistic renders</p>
</div>
<div class="abs exp-card" style="left:755px">
  <div class="exp-icon"><svg width="48" height="48" viewBox="0 0 48 48"><circle cx="30" cy="24" r="8" fill="none" stroke="#fff" stroke-width="3"/><circle cx="30" cy="24" r="3" fill="#fff"/><path d="M30 12v-4M30 40v-4M42 24h4M14 24h4M8 10v28M4 16h8M4 30h8" stroke="#fff" stroke-width="3"/></svg></div>
  <h3>Design for Manufacture</h3>
  <p>Creating designs optimised for prototype and production manufacture</p>
</div>
<a class="btn" style="left:481px;top:3047px;width:230px;height:42px">View All Expertise</a>

<h2 class="section-title" style="top:3278px;font-size:50px;line-height:58px">FEEDBACK FROM SOME OF OUR<br><span class="hl">RECENT CUSTOMERS</span></h2>
<p class="section-sub" style="top:3414px;left:310px;width:580px">Real feedback from clients who trust us to deliver high-quality mechanical design and engineering solutions.</p>

<div class="abs arrow" style="left:63px;top:3685px"><svg width="14" height="14"><path d="M9 2L4 7l5 5" fill="none" stroke="#222" stroke-width="2.2"/></svg></div>
<div class="abs arrow" style="left:1069px;top:3685px;border-color:var(--blue)"><svg width="14" height="14"><path d="M5 2l5 5-5 5" fill="none" stroke="#2f55f0" stroke-width="2.2"/></svg></div>

<article class="abs review" style="left:145px">
  <span class="review-mark"></span>
  <div class="stars"><svg width="90" height="16" viewBox="0 0 90 16" fill="#2f55f0"><path id="st" d="M8 0l2.4 5 5.6.6-4.2 3.8 1.2 5.6L8 12.2 3 15l1.2-5.6L0 5.6 5.6 5z"/><use href="#st" x="18"/><use href="#st" x="36"/><use href="#st" x="54"/><use href="#st" x="72"/></svg></div>
  <p>"Daniel is able to bridge the gap between what management want and what manufacturing can deliver.<br>In the field of Casting his intuition for the nuances and knowledge of casting technical nuances means he is able to push both the design and guide manufacturers to produce excellent results."</p>
  <span class="avatar" role="img" aria-label="Customer portrait"></span>
  <h4>Owen Hartley<br>Design Engineer</h4>
</article>
<article class="abs review" style="left:455px">
  <span class="review-mark"></span>
  <div class="stars"><svg width="90" height="16" viewBox="0 0 90 16" fill="#2f55f0"><use href="#st"/><use href="#st" x="18"/><use href="#st" x="36"/><use href="#st" x="54"/><use href="#st" x="72"/></svg></div>
  <p>"Daniel is able to bridge the gap between what management want and what manufacturing can deliver.<br>In the field of Casting his intuition for the nuances and knowledge of casting technical nuances means he is able to push both the design and guide manufacturers to produce excellent results."</p>
  <span class="avatar" role="img" aria-label="Customer portrait" style="background:linear-gradient(180deg,#7a4f30,#e3bfa0)"></span>
  <h4>Hannah Reeve<br>Client</h4>
</article>
<article class="abs review" style="left:765px">
  <span class="review-mark"></span>
  <div class="stars"><svg width="90" height="16" viewBox="0 0 90 16" fill="#2f55f0"><use href="#st"/><use href="#st" x="18"/><use href="#st" x="36"/><use href="#st" x="54"/><use href="#st" x="72"/></svg></div>
  <p>Daniel's support, patience and thorough explanation of the technical challenges through the complex development process allowed me as the Project Manager to confidently manage both the supplier and the customers' expectations daily from an informed and knowledgeable position and made my job so much easier</p>
  <span class="avatar" role="img" aria-label="Customer portrait" style="background:linear-gradient(180deg,#3e4652,#c8b4a4)"></span>
  <h4>Simon Ashdown<br>Project Manager</h4>
</article>

<section class="abs trust">
  <h2>ENGINEERING<br>THAT BUILDS TRUST</h2>
  <p class="lead">We don't just design; we solve. Our approach combines deep technical knowledge with creative problem solving to deliver results that are manufacturable, cost effective, and market-ready.</p>
  <div class="feature" style="left:48px;top:268px"><i><svg width="22" height="22"><circle cx="11" cy="11" r="8" fill="none" stroke="#2f55f0" stroke-width="2.5"/><path d="M11 6v5l3 2" stroke="#2f55f0" stroke-width="2.5" fill="none"/></svg></i><div><b>RAPID ITERATION</b><span>Fast prototyping cycles to validate concepts early.</span></div></div>
  <div class="feature" style="left:266px;top:268px"><i><svg width="22" height="22"><path d="M11 2l8 3v6c0 5-4 8-8 9-4-1-8-4-8-9V5z" fill="#2f55f0"/></svg></i><div><b>IP PROTECTION</b><span>Strict confidentiality and secure data handling.</span></div></div>
  <div class="feature" style="left:48px;top:362px"><i><svg width="22" height="22"><circle cx="7" cy="7" r="3" fill="#2f55f0"/><circle cx="15" cy="7" r="3" fill="#2f55f0"/><path d="M2 19c0-5 10-5 10 0M10 19c0-5 10-5 10 0" fill="#2f55f0"/></svg></i><div><b>COLLABORATIVE</b><span>We work as an extension of your internal team.</span></div></div>
  <div class="feature" style="left:266px;top:362px"><i><svg width="22" height="22"><circle cx="11" cy="9" r="6" fill="none" stroke="#2f55f0" stroke-width="2.5"/><path d="M7 14l-2 7 6-3 6 3-2-7" fill="#2f55f0"/></svg></i><div><b>QUALITY ASSURED</b><span>ISO 9001 compliant processes and Standards.</span></div></div>

  <div class="chart-card">
    <h3>Industry Distribution</h3>
    <svg class="abs" style="left:72px;top:86px" width="260" height="260" viewBox="-130 -130 260 260" font-family="Inter,sans-serif" font-size="11" fill="#fff" text-anchor="middle">
      <path d="M0 0L0 -130A130 130 0 0 1 123.6 40.2Z" fill="#d1174a"/>
      <path d="M0 0L123.6 40.2A130 130 0 0 1 76.4 105.2Z" fill="#ef8aa1"/>
      <path d="M0 0L76.4 105.2A130 130 0 0 1 -40.2 123.6Z" fill="#f4a8ba"/>
      <path d="M0 0L-40.2 123.6A130 130 0 0 1 -130 0Z" fill="#e8426c"/>
      <path d="M0 0L-130 0A130 130 0 0 1 0 -130Z" fill="#e2264f"/>
      <g stroke="#fff" stroke-width="1.5"><path d="M0 0V-130M0 0L123.6 40.2M0 0L76.4 105.2M0 0L-40.2 123.6M0 0H-130"/></g>
      <text x="58" y="-48">Medical</text><text x="58" y="-35">30%</text>
      <text x="68" y="46" transform="rotate(36 68 46)">Automotive</text><text x="62" y="58" transform="rotate(36 62 58)">10%</text>
      <text x="14" y="74">Aerospace</text><text x="14" y="87">15%</text>
      <text x="-68" y="40">Industrial</text><text x="-68" y="53">20%</text>
      <text x="-56" y="-56">Consumer</text><text x="-56" y="-43">25%</text>
    </svg>
    <p>Serving diverse sectors with specialized<br>mechanical expertise</p>
  </div>
</section>

<svg class="abs footer-curve" viewBox="0 0 1200 130" preserveAspectRatio="none"><path d="M0 90C400 40 800 15 1200 0V130H0Z" fill="#555b6a"/><path d="M0 70C400 52 800 40 1200 28V130H0Z" fill="#2f55f0"/><path d="M0 100C400 70 800 55 1200 46V130H0Z" fill="#0a1240"/></svg>
<footer class="abs footer"></footer>
<div class="abs footer-brand"><i></i><span>Valtro Build</span></div>
<p class="abs footer-about">Precision mechanical design and engineering consultancy delivering innovative solutions for complex challenges.</p>
<div class="abs socials" aria-label="Social media links"><i></i><i></i><i></i><i></i></div>
<div class="abs footer-col" style="left:597px"><h5>Quick Links</h5><ul><li>Services</li><li>Portfolio</li><li>About</li><li>Contac</li></ul></div>
<div class="abs footer-col" style="left:755px"><h5>Legal</h5><ul style="padding-left:12px"><li>Privacy Policy</li><li>Terms of Service</li></ul></div>
<p class="abs legal-line" style="left:145px">© 2024 Valtro Build Design. All rights reserved.</p>
<p class="abs legal-line" style="left:849px;width:200px;text-align:right">Built with precision and care</p>

</body>
</html>
```